Menu Design Project

We trying to replace old flyer/menu with some new design.
hello this is my old menu i attached in email and my logo, the text you can pick from the menu and and i also attached some new picture for the food ,with my menu size unfold. front and back and then fold to 3.5" * 11". please show me what best can you do .Trifold is fine but must have image of food,
this is indian Restaurant
thats fine to have trifold menu design do to short time

Need to add also food picture on menu

Font styles to use
Serif
Decorative
Script

Colors

Designer to choose colors to be used in the design.

Requirements
Must have
• food image on menu
• trifold is fine ( do to short time)
• menu has to elegant ,color or text can be optional, Menu need to be neat and clean no too much rush on between the words .

```html
<!DOCTYPE html>
<html lang="en">
<head>
<meta charset="utf-8">
<title>Saffron Court – Trifold Menu</title>
<link rel="stylesheet" href="https://fonts.googleapis.com/css2?family=Kaushan+Script&family=Libre+Baskerville:wght@400;700&display=swap">
<style>
:root{
  --page:#e6e6e4;
  --ink:#0d0c0c;
  --red:#b5141c;
  --red-dark:#5e0a0e;
  --cream:#f1ebdf;
  --muted:#b9b2a6;
  --gold:#f3c614;
  --serif:"Libre Baskerville",Georgia,serif;
  --script:"Kaushan Script",cursive;
}
*{box-sizing:border-box;margin:0;padding:0}
html,body{width:878px;height:1200px;overflow:hidden;background:var(--page)}
body{position:relative;font-family:var(--serif);color:var(--cream)}
.sheet{position:absolute;left:30px;width:818px;height:534px;background:var(--ink);display:flex;padding:14px 10px 12px;box-shadow:0 2px 8px rgba(0,0,0,.35)}
.sheet--outside{top:42px}
.sheet--inside{top:622px}
.panel{width:264px;display:flex;flex-direction:column;padding:0 6px}
.panel + .panel{margin-left:5px}
.heading{display:flex;align-items:center;justify-content:center;height:34px;margin:4px 0 8px}
.flourish{width:30px;height:26px;border-radius:50% 10% 50% 10%;background:radial-gradient(circle,var(--red) 20%,var(--red-dark) 70%,transparent 72%)}
.flourish--right{transform:scaleX(-1)}
.heading h2{font-family:var(--script);font-weight:400;font-size:13px;color:var(--cream);border:1.5px solid var(--red);outline:1px solid var(--red-dark);outline-offset:2px;padding:2px 12px;margin:0 3px;white-space:nowrap;letter-spacing:.3px}
.cols{display:grid;grid-template-columns:1fr 1fr;column-gap:10px}
.item{display:grid;grid-template-columns:1fr auto;column-gap:4px;margin-bottom:8px}
.item b{font-weight:700;font-size:5.4px;text-transform:uppercase;letter-spacing:.2px}
.item i{font-style:normal;font-size:5.4px}
.item small{grid-column:1/-1;font-size:4.1px;line-height:1.3;color:var(--muted)}
.cols--tight .item{margin-bottom:5px}
.cols--rule{border-left:0}
.cols--rule > div + div{border-left:1px dotted #555;padding-left:8px}
.note{margin-top:auto;text-align:center;font-size:5px;color:var(--red)}
.address{margin-top:auto;text-align:center;font-size:7px;line-height:1.45}
.address span{display:block}
.brand{display:flex;flex-direction:column;align-items:center;padding-top:26px}
.brand-mark{width:46px;height:46px;border-radius:50%;background:var(--cream);margin-bottom:10px}
.brand-name{font-family:var(--script);font-size:21px;color:var(--cream);font-weight:400}
.photo-frame{margin:22px auto 0;width:170px;padding:8px;border:2px solid var(--red);outline:1px solid var(--red-dark);outline-offset:3px}
.interior-photo{height:150px;background:linear-gradient(180deg,#6e5a3a 0%,#b59a6e 40%,#d9cdb6 65%,#7a6148 100%)}
.hours-title{margin-top:46px;font-family:var(--script);font-size:11px;text-align:center;border-top:1px solid var(--red);border-bottom:1px solid var(--red);width:130px;margin-left:auto;margin-right:auto;padding:1px 0}
.hours{display:flex;justify-content:space-between;margin-top:14px;text-align:center}
.hours b{display:block;color:var(--gold);font-size:6px}
.hours span{font-size:4.5px;color:var(--cream)}
.website{margin-top:18px;text-align:center;font-family:var(--script);font-size:9px}
.dishes{position:relative;margin-top:auto;height:180px}
.dish{position:absolute;border-radius:50%;border:2px solid var(--red)}
.dish--wings{left:42px;top:8px;width:118px;height:80px;background:radial-gradient(ellipse,#c0522a 20%,#6e2410 70%)}
.dish--rice{left:14px;top:98px;width:94px;height:64px;background:radial-gradient(ellipse,#d4a35a 20%,#6b4a22 70%)}
.dish--bread{left:140px;top:84px;width:106px;height:72px;background:radial-gradient(ellipse,#e2b46a 20%,#7a4e1e 70%)}
</style>
</head>
<body>

<section class="sheet sheet--outside">
  <div class="panel">
    <div class="heading"><span class="flourish" role="img" aria-label="Red scroll ornament"></span><h2>Handise (Vegetarien)</h2><span class="flourish flourish--right" role="img" aria-label="Red scroll ornament"></span></div>
    <div class="cols">
      <div>
        <div class="item"><b>Paneer Makhni</b><i>$8.50</i><small>fresh home made cheese folded into creamy tomato sauce</small></div>
        <div class="item"><b>Paneer Tikka Masala</b><i>$8.50</i><small>cottage cheese sauteed with bell pepper, onion in spiced tomato sauce</small></div>
        <div class="item"><b>Kadai Paneer</b><i>$8.50</i><small>home made cubes of cheese stir fry in a kadai with ginger and pepper</small></div>
        <div class="item"><b>Palak Paneer</b><i>$7.99</i><small>fresh spinach cooked with cubes of cheese and garlic</small></div>
        <div class="item"><b>Mutter Paneer</b><i>$7.99</i><small>home made cheese cooked with green peas in mild sauce</small></div>
        <div class="item"><b>Shahi Paneer</b><i>$8.50</i><small>paneer cubes cooked in a rich creamy almond sauce</small></div>
        <div class="item"><b>Paneer Bhurji</b><i>$10.99</i><small>grated home made cheese cooked with green pepper and onions</small></div>
        <div class="item"><b>Malai Kofta</b><i>$8.50</i><small>cheese vegetable balls in a savory almond flavored sauce</small></div>
        <div class="item"><b>Navratan Korma</b><i>$8.50</i><small>combination of vegetables and fruit cooked in a cashew sauce</small></div>
        <div class="item"><b>Kaju Mushroom Mutter</b><i>$8.50</i><small>mushroom, cashew and peas cooked in onion gravy</small></div>
        <div class="item"><b>Methi Malai Mutter</b><i>$8.50</i><small>fenugreek leaves cooked with peas in cashew flavor sauce</small></div>
        <div class="item"><b>Aloo Gobhi</b><i>$7.50</i><small>a dry dish made with potatoes, cauliflower and ginger</small></div>
      </div>
      <div>
        <div class="item"><b>Bhindi Masala</b><i>$7.50</i><small>fresh okra sauteed with brown onion and tomatoes</small></div>
        <div class="item"><b>Achari Baigan</b><i>$7.99</i><small>baby eggplant cooked in a spicy pickled flavor masala</small></div>
        <div class="item"><b>Baigan Bhartha</b><i>$7.50</i><small>eggplant roasted on charcoal, minced with onions and tomatoes</small></div>
        <div class="item"><b>Vegetable Jalfrezi</b><i>$7.50</i><small>mixed vegetable with cottage cheese mildly spiced</small></div>
        <div class="item"><b>Zeera Aloo</b><i>$7.50</i><small>crispy potato stir fry with cumin seeds</small></div>
        <div class="item"><b>Sarson Ka Saag</b><i>$7.99</i><small>mustard leaves cooked in Punjabi style, served with makki roti</small></div>
        <div class="item"><b>Chana Peshawari</b><i>$7.50</i><small>chickpeas cooked in an exotic blend of Indian spices</small></div>
        <div class="item"><b>Chana Palak</b><i>$7.99</i><small>chick peas cooked with fresh spinach</small></div>
        <div class="item"><b>Punjabi Kadi</b><i>$7.50</i><small>a stew made with yogurt and chickpea flour dumplings</small></div>
        <div class="item"><b>Daal Tarka Yellow</b><i>$7.50</i><small>yellow lentils sauteed with tomato, ginger and garlic</small></div>
        <div class="item"><b>Daal Tarka Black</b><i>$7.50</i><small>black lentils sauteed with tomato, ginger and garlic</small></div>
        <div class="item"><b>Daal Makhni</b><i>$7.50</i><small>lentils with kidney beans simmered in tomato and butter</small></div>
      </div>
    </div>
    <div class="heading"><span class="flourish" role="img" aria-label="Red scroll ornament"></span><h2>Biryani &amp; Rise</h2><span class="flourish flourish--right" role="img" aria-label="Red scroll ornament"></span></div>
    <div class="cols cols--tight">
      <div>
        <div class="item"><b>Chicken Biryani</b><i>$7.99</i><small>boneless chicken cooked on low heat with long grain basmati rice</small></div>
        <div class="item"><b>Goat Biryani</b><i>$9.50</i><small>goat cooked on low heat with long grain basmati rice</small></div>
        <div class="item"><b>Lamb Biryani</b><i>$9.99</i><small>lamb cooked on low heat with long grain basmati rice</small></div>
        <div class="item"><b>Shrimp Biryani</b><i>$10.99</i><small>shrimp cooked on low heat with basmati rice</small></div>
      </div>
      <div>
        <div class="item"><b>Vegetable Biryani</b><i>$7.50</i><small>basmati rice cooked with mixed vegetable and herbs</small></div>
        <div class="item"><b>Zeera Rice</b><i>$3.99</i><small>basmati rice cooked with cumin, herbs and saffron</small></div>
        <div class="item"><b>Peas Pulao</b><i>$5.99</i></div>
        <div class="item"><b>Royal Spl. Biryani</b><i>$11.99</i><small>fresh okra sauteed with brown onion and tomatoes</small></div>
      </div>
    </div>
    <p class="note">[Prices subject to change without Notice Tax is not included in these prices]</p>
  </div>

  <div class="panel">
    <div class="heading"><span class="flourish" role="img" aria-label="Red scroll ornament"></span><h2>Tandoori Bread</h2><span class="flourish flourish--right" role="img" aria-label="Red scroll ornament"></span></div>
    <div class="cols cols--tight">
      <div>
        <div class="item"><b>Tandoori Roti</b><i>$1.75</i><small>flat whole wheat bread baked in a clay oven</small></div>
        <div class="item"><b>Tandoori Naan</b><i>$1.75</i><small>soft white bread baked in a clay oven</small></div>
        <div class="item"><b>Garlic Naan</b><i>$2.50</i><small>naan flavored with fresh garlic and coriander</small></div>
        <div class="item"><b>Lachha Paratha</b><i>$2.50</i><small>multilayered whole wheat bread baked in oven</small></div>
        <div class="item"><b>Onion Kulcha</b><i>$2.99</i><small>naan stuffed with seasoned finely chopped onions</small></div>
      </div>
      <div>
        <div class="item"><b>Aloo Paratha</b><i>$2.99</i><small>whole wheat paratha stuffed with mildly spiced mashed potato</small></div>
        <div class="item"><b>Gobhi Paratha</b><i>$3.50</i><small>wheat bread stuffed with mildly spiced cauliflower</small></div>
        <div class="item"><b>Pudina Paratha</b><i>$2.99</i><small>tandoori paratha flavored with fresh mint</small></div>
        <div class="item"><b>Keema Naan</b><i>$3.99</i><small>white bread stuffed with fresh chicken keema</small></div>
        <div class="item"><b>Jalebi Paratha</b><i>$2.99</i><small>rich multilayered naan bread</small></div>
      </div>
    </div>
    <div class="heading"><span class="flourish" role="img" aria-label="Red scroll ornament"></span><h2>Desserts</h2><span class="flourish flourish--right" role="img" aria-label="Red scroll ornament"></span></div>
    <div class="cols cols--tight">
      <div>
        <div class="item"><b>Rice Kheer</b><i>$3.99</i><small>pudding flavored with cardamom, nuts, raisins and topped with nuts</small></div>
        <div class="item"><b>Ras Malai</b><i>$3.99</i><small>dumpling flavored with cardamom, saffron and topped with pistachio</small></div>
        <div class="item"><b>Kulfi</b><i>$3.99</i><small>set cooked with milk cottage, cheese and nuts</small></div>
      </div>
      <div>
        <div class="item"><b>Gulab Jamun (3 pc.)</b><i>$3.99</i><small>golden fried balls of milk pastry soaked in honey syrup topped with coconut</small></div>
        <div class="item"><b>Ice Cream</b><i>$3.99</i><small>mango or vanilla or chocolate flavor</small></div>
      </div>
    </div>
    <div class="heading"><span class="flourish" role="img" aria-label="Red scroll ornament"></span><h2>Beverages</h2><span class="flourish flourish--right" role="img" aria-label="Red scroll ornament"></span></div>
    <div class="cols cols--tight">
      <div>
        <div class="item"><b>Mango Lassi</b><i>$3.50</i><small>a refreshing yogurt mango drink</small></div>
        <div class="item"><b>Lassi (sweet or salted)</b><i>$3.50</i><small>a delicious yogurt drink</small></div>
        <div class="item"><b>Fresh Lemonade</b><i>$2.99</i><small>a sweet and sour lemon flavor drink</small></div>
        <div class="item"><b>Pina Colada Virgin</b><i>$3.99</i><small>combination of pineapple juice and coconut cream</small></div>
        <div class="item"><b>Strawberry Daiquiri Virgin</b><i>$3.99</i><small>an ambrosial blend of strawberries and citrus soda, ideal for a hot summer day</small></div>
        <div class="item"><b>Orange Juice</b><i>$2.99</i></div>
      </div>
      <div>
        <div class="item"><b>Pineapple Juice</b><i>$2.99</i></div>
        <div class="item"><b>Mango Juice</b><i>$2.99</i></div>
        <div class="item"><b>Masala Tea</b><i>$1.99</i><small>Indian tea with a mixture of aromatic Indian spices</small></div>
        <div class="item"><b>Coffee</b><i>$1.99</i></div>
        <div class="item"><b>Cold Beers</b><i></i><small>assorted domestic &amp; imported lagers</small></div>
        <div class="item"><b>Indian Beers</b><i>$1.99</i><small>Indian lagers</small></div>
        <div class="item"><b>Wines (750ml / 1.5 Ltr)</b><i>$22.00/$38.00</i><small>Merlot, Cabernet, Chardonnay, Pinot Grigio</small></div>
        <div class="item"><b>Cola, Lemon Soda, Ginger Ale</b><i>$1.50</i></div>
      </div>
    </div>
    <p class="address">
      <span>42-10 Garden Lane, Maple Heights, NY 10000</span>
      <span>Tel: 555-014-2200, 555-014-2201</span>
      <span>Fax: 555-014-2202</span>
    </p>
  </div>

  <div class="panel">
    <div class="brand">
      <span class="brand-mark"></span>
      <h1 class="brand-name">Saffron Court</h1>
    </div>
    <div class="photo-frame">
      <div class="interior-photo" role="img" aria-label="Photo of the restaurant dining room with booths and tiled floor"></div>
    </div>
    <h3 class="hours-title">Business Hours</h3>
    <div class="hours">
      <p><b>Lunch Hours:</b><span>Mon - Sun 11:30am - 3:30pm</span></p>
      <p><b>Dinner Hours:</b><span>Mon - Sun 3:30pm - 11:00pm</span></p>
      <p><b>Lunch Special:</b><span>Mon - Sun 11:30 AM - 04:00 PM</span></p>
    </div>
    <p class="website">www.saffroncourtdining.com</p>
  </div>
</section>

<section class="sheet sheet--inside">
  <div class="panel">
    <div class="heading"><span class="flourish" role="img" aria-label="Red scroll ornament"></span><h2>Vegetarian Appetize</h2><span class="flourish flourish--right" role="img" aria-label="Red scroll ornament"></span></div>
    <div class="cols cols--rule">
      <div>
        <div class="item"><b>Vegetable Samosa (2 pc.)</b><i>$2.99</i><small>spicy seasoned potatoes &amp; peas wrapped in light pastry</small></div>
        <div class="item"><b>Samosa Chaat (2 pc.)</b><i>$6.99</i><small>samosa served with chutney &amp; chickpea</small></div>
        <div class="item"><b>Aloo Tikki Chaat (4 pc.)</b><i>$6.99</i><small>aloo tikki served with chutney &amp; chickpea</small></div>
        <div class="item"><b>Mix Veg. Pakora</b><i>$6.50</i><small>deep fried vegetable fritters dipped in chick peas flour</small></div>
        <div class="item"><b>Papri Chaat</b><i>$6.50</i><small>mixture of crisp flour crackers served with potato, chick peas and yogurt</small></div>
        <div class="item"><b>Dahi Bhalla</b><i>$6.99</i><small>softball of mix lentils topped with yogurt, mint &amp; tamarind sauce</small></div>
      </div>
      <div>
        <div class="item"><b>Paneer Pakora (7 pc.)</b><i>$8.50</i><small>deep fried cottage cheese fritters dipped in chick peas flour</small></div>
        <div class="item"><b>Vegetable Seekh Kabab</b><i>$8.99</i><small>minced vegetable with cottage cheese seasoned with fresh herbs</small></div>
        <div class="item"><b>Paneer Tikka Tandoori</b><i>$11.99</i><small>grilled paneer cheese, bell pepper, onion with ginger flavor yogurt</small></div>
        <div class="item"><b>Chhole Bhature (2 pc.)</b><i>$7.99</i><small>large puffy shallow fried bread served with chick peas</small></div>
        <div class="item"><b>Stuffed Paneer Pakora (6 pc.)</b><i>$8.50</i><small>home made cheese stuffed with mixture of spiced potato &amp; mint</small></div>
        <div class="item"><b>Chatpati Aloo Chaat</b><i>$7.50</i></div>
      </div>
    </div>
    <div class="heading"><span class="flourish" role="img" aria-label="Red scroll ornament"></span><h2>Non Vegetarian Appetizer</h2><span class="flourish flourish--right" role="img" aria-label="Red scroll ornament"></span></div>
    <div class="cols cols--rule">
      <div>
        <div class="item"><b>Chicken Samosa (2 pc.)</b><i>$5.99</i><small>spicy chicken &amp; peas wrapped in a light pastry</small></div>
        <div class="item"><b>Chicken Pakora</b><i>$10.99</i><small>mildly spiced chicken fritters</small></div>
        <div class="item"><b>Fish Amritsari</b><i>$11.99</i><small>mildly spiced boneless fish fritters</small></div>
        <div class="item"><b>Tawa Chicken</b><i>$12.99</i><small>bar cue chicken sauteed with bell pepper and onion in chef sauce</small></div>
        <div class="item"><b>Garlic Shrimp</b><i>$12.99</i><small>shrimp cooked in white wine and chef special garlic sauce</small></div>
        <div class="item"><b>Spicy Wings (8 pc.)</b><i>$8.99</i><small>hot and spicy buffalo wings all time favorite</small></div>
        <div class="item"><b>Tandoori Chicken</b><i>$7.99</i><small>chicken marinated in yogurt and mild spices cooked in clay oven</small></div>
        <div class="item"><b>Lemon Chicken</b><i>$10.99</i><small>chicken cooked with mild spices, lemon and mango powder</small></div>
        <div class="item"><b>Chicken Seekh Kabab</b><i>$9.50</i><small>ground chicken seasoned with fresh herbs, rolled on skewer</small></div>
        <div class="item"><b>Lamb Seekh Kabab</b><i>$11.99</i><small>ground lamb seasoned with fresh herbs, rolled on skewer</small></div>
      </div>
      <div>
        <div class="item"><b>Chicken Tikka</b><i>$10.50</i><small>boneless pieces of chicken seasoned with fresh herbs and yogurt cooked in oven</small></div>
        <div class="item"><b>Chicken Malai Kabab</b><i>$10.99</i><small>boneless tender pieces of chicken marinated in sour cream</small></div>
        <div class="item"><b>Achari Tikka</b><i>$10.50</i><small>tender pieces of chicken marinated in pickle flavor sauce</small></div>
        <div class="item"><b>Afghani Chicken</b><i>$12.99</i><small>mildly spiced chicken with sour cream cooked on a small fire</small></div>
        <div class="item"><b>Fish Tikka Tandoori</b><i>$11.99</i><small>cubes of fish marinated in fresh herbs and ginger, grilled in tandoor</small></div>
        <div class="item"><b>Salmon Fish</b><i>$13.50</i><small>cubes of salmon marinated in fresh herbs, grilled in tandoor</small></div>
        <div class="item"><b>Tawa Fish</b><i>$12.99</i><small>small pieces of fish seasoned in yogurt and fresh herbs</small></div>
        <div class="item"><b>Tandoori Shrimp (6 pc.)</b><i>$14.99</i><small>jumbo shrimp marinated in yogurt, mild spices and herbs</small></div>
        <div class="item"><b>Lamb Chop (5 pc.)</b><i>$21.99</i><small>rack of lamb marinated in traditional herbs, roasted on skewers</small></div>
        <div class="item"><b>Tandoori Mix Grill</b><i>$17.99</i><small>delicious combination of grilled chicken, seekh kabab and shrimp</small></div>
      </div>
    </div>
  </div>

  <div class="panel">
    <div class="heading"><span class="flourish" role="img" aria-label="Red scroll ornament"></span><h2>Indo Chinese</h2><span class="flourish flourish--right" role="img" aria-label="Red scroll ornament"></span></div>
    <div class="cols cols--rule">
      <div>
        <div class="item"><b>Chilli Paneer</b><i>$10.99</i><small>cottage cheese sauteed with bell pepper &amp; onion in Chinese spicy sauce</small></div>
        <div class="item"><b>Chilli Mushroom</b><i>$10.99</i><small>mushroom sauteed with bell pepper &amp; onion in Chinese sauce</small></div>
        <div class="item"><b>Chilli Gobhi</b><i>$9.99</i><small>gobhi sauteed with bell pepper &amp; onion in Chinese sauce</small></div>
        <div class="item"><b>Vegetable Manchurian</b><i>$9.50</i><small>mix vegetable balls cooked in chef special garlic sauce</small></div>
        <div class="item"><b>Vegetable Chowmin</b><i>$7.99</i><small>stir fry noodles with thin sliced vegetables in Chinese sauce</small></div>
        <div class="item"><b>Vegetable Spring Roll</b><i>$6.99</i><small>carrots, red bell pepper, bean sprouts wrapped in spring rolls</small></div>
      </div>
      <div>
        <div class="item"><b>Chilli Chicken</b><i>$10.99</i><small>chicken pieces sauteed with bell pepper and onion in spicy sauce</small></div>
        <div class="item"><b>Chilli Fish</b><i>$11.99</i><small>fish fritters sauteed with bell peppers and onion</small></div>
        <div class="item"><b>Chilli Shrimp</b><i>$12.99</i><small>shrimp with bell pepper and onion cooked in spicy sauce</small></div>
        <div class="item"><b>Chicken Manchurian</b><i>$10.99</i><small>chicken balls cooked in a semi thick garlic flavor sauce</small></div>
        <div class="item"><b>Chicken Chowmin</b><i>$9.99</i><small>stir fry noodles and thin sliced vegetables with chicken</small></div>
      </div>
    </div>
    <div class="heading"><span class="flourish" role="img" aria-label="Red scroll ornament"></span><h2>Soup, Salad &amp; Raita</h2><span class="flourish flourish--right" role="img" aria-label="Red scroll ornament"></span></div>
    <div class="cols cols--rule cols--tight">
      <div>
        <div class="item"><b>Tomato Soup</b><i>$3.99</i><small>a simple soup made with fresh tomatoes</small></div>
        <div class="item"><b>Vegetarian Soup</b><i>$3.99</i><small>a soup made with variety of vegetables</small></div>
        <div class="item"><b>Chicken Soup</b><i>$4.50</i><small>classic chicken soup of a clear broth with small pieces of chicken</small></div>
        <div class="item"><b>Hot N Sour Soup</b><i>$4.99</i><small>a soup of spicy and sour flavors</small></div>
      </div>
      <div>
        <div class="item"><b>Fresh Garden Salad</b><i>$4.50</i></div>
        <div class="item"><b>Masala Salad</b><i>$5.99</i><small>house special</small></div>
        <div class="item"><b>Mix Raita</b><i>$3.99</i></div>
        <div class="item"><b>Boondi Raita</b><i>$3.99</i></div>
        <div class="item"><b>Pudina Raita</b><i>$3.99</i></div>
        <div class="item"><b>Plain Dahi</b><i>$3.50</i></div>
      </div>
    </div>
    <div class="heading"><span class="flourish" role="img" aria-label="Red scroll ornament"></span><h2>Seafood Special</h2><span class="flourish flourish--right" role="img" aria-label="Red scroll ornament"></span></div>
    <div class="cols cols--rule cols--tight">
      <div>
        <div class="item"><b>Kadai Fish</b><i>$11.99</i><small>boneless fish sauteed with bell pepper, onion and tomato</small></div>
        <div class="item"><b>Fish Curry</b><i>$11.99</i><small>a delicious fish curry which is both rich and aromatic</small></div>
        <div class="item"><b>Fish Masala</b><i>$11.99</i><small>fish cooked with fresh garlic and tomato</small></div>
        <div class="item"><b>Goa Fish Curry</b><i>$11.99</i><small>fish curry made in this style is tangy and spicy</small></div>
        <div class="item"><b>Fish Tikka Masala</b><i>$11.99</i><small>roasted fish in a rich red creamy lightly spiced sauce</small></div>
        <div class="item"><b>Shrimp Curry</b><i>$12.99</i><small>cooked with fresh ginger, onion and tomato gravy</small></div>
      </div>
      <div>
        <div class="item"><b>Shrimp Masala</b><i>$12.99</i><small>jumbo shrimp seasoned with chili and lemon juice</small></div>
        <div class="item"><b>Shrimp Saag</b><i>$12.99</i><small>shrimp cooked with fresh spinach</small></div>
        <div class="item"><b>Shrimp Bhuna</b><i>$12.99</i><small>shrimp cooked with shredded onions, peppers and spices</small></div>
        <div class="item"><b>Shrimp Vindaloo</b><i>$12.99</i><small>shrimp cooked with potato, vinegar and hot red chilli</small></div>
        <div class="item"><b>Kadai Shrimp</b><i>$12.99</i><small>shrimp sauteed with ginger, onion, fresh tomatoes and spices</small></div>
      </div>
    </div>
  </div>

  <div class="panel">
    <div class="heading"><span class="flourish" role="img" aria-label="Red scroll ornament"></span><h2>Handi Special (Non-Veg)</h2><span class="flourish flourish--right" role="img" aria-label="Red scroll ornament"></span></div>
    <div class="cols cols--rule">
      <div>
        <div class="item"><b>Chicken Makhni</b><i>$8.99</i><small>chicken pieces roasted in a clay oven &amp; folded into tomato sauce</small></div>
        <div class="item"><b>Tikka Masala</b><i>$8.99</i><small>chunks of roasted chicken sauteed with bell pepper in spiced sauce</small></div>
        <div class="item"><b>Chicken Curry</b><i>$8.99</i><small>all time favorite chicken, fresh ginger, onion and tomato gravy</small></div>
        <div class="item"><b>Chicken Korma</b><i>$8.99</i><small>boneless chicken cooked in a rich cashew and onion sauce</small></div>
        <div class="item"><b>Kadai Chicken</b><i>$8.99</i><small>chicken sauteed with bell pepper, onion and fresh tomato</small></div>
        <div class="item"><b>Chicken Saag</b><i>$8.99</i><small>chicken cooked with fresh spinach</small></div>
        <div class="item"><b>Chicken Jalfrezi</b><i>$8.99</i><small>grilled cubes of chicken breast sauteed with fresh vegetables</small></div>
        <div class="item"><b>Chicken Masala</b><i>$8.99</i><small>savory chicken seasoned with chili and lemon juice</small></div>
        <div class="item"><b>Chicken Vindaloo</b><i>$8.99</i><small>cubes of chicken cooked with onion and potato in hot sauce</small></div>
        <div class="item"><b>Goat Curry</b><i>$9.99</i><small>traditional offering, a special blend of goat on bones and spices</small></div>
        <div class="item"><b>Goat Masala</b><i>$10.99</i><small>baby goat seasoned with chili &amp; lemon juice in exotic spices</small></div>
      </div>
      <div>
        <div class="item"><b>Kadai Goat</b><i>$9.99</i><small>goat sauteed with bell pepper, onion and fresh tomato</small></div>
        <div class="item"><b>Goat Saag</b><i>$9.99</i><small>goat cooked with fresh spinach</small></div>
        <div class="item"><b>Goat Vindaloo</b><i>$9.99</i><small>cooked with potato, vinegar and hot red chili peppers</small></div>
        <div class="item"><b>Chicken Keema Mutter</b><i>$10.99</i><small>ground chicken cooked with green peas and fresh ginger</small></div>
        <div class="item"><b>Lamb Curry</b><i>$10.99</i><small>a dish from Northern India, among the most popular curries</small></div>
        <div class="item"><b>Lamb Rogan Josh</b><i>$10.99</i><small>boneless lamb cooked in Kashmir style</small></div>
        <div class="item"><b>Lamb Saag</b><i>$10.99</i><small>lamb cooked with fresh spinach</small></div>
        <div class="item"><b>Lamb Korma</b><i>$10.99</i><small>lamb cooked in light cream, almond and cashew nut sauce</small></div>
        <div class="item"><b>Lamb Bhuna Ghost</b><i>$10.99</i><small>tender lamb prepared with fresh ginger, onions and peppers</small></div>
        <div class="item"><b>Lamb Vindaloo</b><i>$10.99</i><small>cooked with potato, vinegar and hot red chilli</small></div>
        <div class="item"><b>Lamb Keema Mutter</b><i>$12.99</i><small>minced lamb cooked with peas, onions and herbs</small></div>
      </div>
    </div>
    <div class="dishes">
      <div class="dish dish--wings" role="img" aria-label="Food photo: plate of spicy fried chicken wings"></div>
      <div class="dish dish--rice" role="img" aria-label="Food photo: bowl of biryani rice"></div>
      <div class="dish dish--bread" role="img" aria-label="Food photo: stuffed naan bread slices"></div>
    </div>
  </div>
</section>

</body>
</html>
```